Company director needs a business card design

I am a semi-retired former senior finance executive who sits on a number of public and private company boards and do some consulting work. I work largely with emerging businesses but deal regularly with top end of town lawyers, bankers etc. I need a thoughtful but relatively conservative design which would also resonate with my younger client base. Some colour would be good. Information limited to name, address, office tel, mobile and email.

Industry/Entity Type

Finance

```html
<!DOCTYPE html>
<html lang="en">
<head>
<meta charset="utf-8">
<title>Business Card – Morgan</title>
<link rel="stylesheet" href="https://fonts.googleapis.com/css2?family=Open+Sans:wght@300;400;600&display=swap">
<style>
  :root {
    --backdrop: #1c1c1e;
    --card: #2a2a2c;
    --band: #f4f4f4;
    --accent: #1ea3e6;
    --ink-light: #ffffff;
  }
  * { margin: 0; padding: 0; box-sizing: border-box; }
  html, body {
    width: 1200px;
    height: 800px;
    overflow: hidden;
    background: var(--backdrop);
    font-family: "Open Sans", Arial, sans-serif;
  }
  .canvas {
    position: relative;
    width: 1200px;
    height: 800px;
  }
  .business-card {
    position: absolute;
    left: 180px;
    top: 160px;
    width: 840px;
    height: 480px;
    background: var(--card);
    overflow: hidden;
  }
  .edge-band {
    position: absolute;
    left: 0;
    width: 100%;
    height: 14px;
    background: var(--band);
  }
  .edge-band--top { top: 0; }
  .edge-band--bottom { bottom: 0; }

  .identity {
    position: absolute;
    left: 130px;
    top: 50%;
    transform: translateY(-50%);
    display: flex;
    align-items: center;
    gap: 18px;
  }
  .identity__dot {
    width: 22px;
    height: 22px;
    border-radius: 50%;
    background: var(--accent);
    flex: none;
  }
  .identity__text { line-height: 1.1; }
  .identity__name {
    font-size: 40px;
    font-weight: 600;
    color: var(--ink-light);
    letter-spacing: 0.5px;
  }
  .identity__role {
    font-size: 22px;
    font-weight: 400;
    color: var(--accent);
    margin-top: 4px;
  }

  .contact-list {
    position: absolute;
    left: 470px;
    top: 140px;
    list-style: none;
  }
  .contact-list__item {
    display: flex;
    align-items: center;
    height: 40px;
    gap: 20px;
  }
  .contact-list__icon {
    width: 18px;
    height: 18px;
    flex: none;
    fill: var(--ink-light);
  }
  .contact-list__text {
    font-size: 19px;
    font-weight: 400;
    color: var(--accent);
    letter-spacing: 0.2px;
  }
</style>
</head>
<body>
<main class="canvas">
  <section class="business-card">
    <div class="edge-band edge-band--top"></div>

    <div class="identity">
      <span class="identity__dot"></span>
      <div class="identity__text">
        <p class="identity__name">Morgan</p>
        <p class="identity__role">manager</p>
      </div>
    </div>

    <ul class="contact-list">
      <li class="contact-list__item">
        <svg class="contact-list__icon" viewBox="0 0 24 24" aria-hidden="true"><path d="M6.6 10.8c1.4 2.8 3.8 5.1 6.6 6.6l2.2-2.2c.3-.3.7-.4 1-.2 1.1.4 2.3.6 3.6.6.6 0 1 .4 1 1V20c0 .6-.4 1-1 1C10.6 21 3 13.4 3 4c0-.6.4-1 1-1h3.5c.6 0 1 .4 1 1 0 1.3.2 2.5.6 3.6.1.3 0 .7-.2 1z"/></svg>
        <span class="contact-list__text">3390 7712</span>
      </li>
      <li class="contact-list__item">
        <svg class="contact-list__icon" viewBox="0 0 24 24" aria-hidden="true"><path d="M7 1h10c1.1 0 2 .9 2 2v18c0 1.1-.9 2-2 2H7c-1.1 0-2-.9-2-2V3c0-1.1.9-2 2-2zm0 3v14h10V4H7zm5 15.5a1 1 0 1 0 0 2 1 1 0 0 0 0-2z"/></svg>
        <span class="contact-list__text">00 481 205 637</span>
      </li>
      <li class="contact-list__item">
        <svg class="contact-list__icon" viewBox="0 0 24 24" aria-hidden="true"><path d="M12 2C8.1 2 5 5.1 5 9c0 5.2 7 13 7 13s7-7.8 7-13c0-3.9-3.1-7-7-7zm0 9.5a2.5 2.5 0 1 1 0-5 2.5 2.5 0 0 1 0 5z"/></svg>
        <span class="contact-list__text">42 Harrow Lane, BC</span>
      </li>
      <li class="contact-list__item">
        <svg class="contact-list__icon" viewBox="0 0 24 24" aria-hidden="true"><path d="M2 5h20v14H2V5zm2 2v.5l8 5 8-5V7H4zm0 2.8V17h16V9.8l-8 5-8-5z"/></svg>
        <span class="contact-list__text">email-morgan42@mailbox.net</span>
      </li>
    </ul>

    <div class="edge-band edge-band--bottom"></div>
  </section>
</main>
</body>
</html>
```